Security Company Needs an UPDATED Business Card and Letterhead Design!

I run a security company and would like to have an updated BUSINESS CARD + LETTERHEAD DESIGN.

Please use my UPDATED address below:

2875 E. Thistlewood Drive
Suite 418 Dallas, Texas 75247

Attached is the current business card as reference, and also my logo.

Target Market(s)

High end security users such as Class A buildings, Corporate Campus Locations, Hospitals, High End Retail Centers, Warehousing, Manufacturing and High Tech Companies

Industry/Entity Type

Security Guard

Contact Information for Business Card

Looking for unique, yet professional

Requirements
Must have
• Must use the current logo and incorporate it into any design. Use the colors that are included in the logo. I also need to be able to easily add employees as the company grows. Should be an easy process to change Names and Numbers

```html
<!DOCTYPE html>
<html lang="en">
<head>
<meta charset="utf-8">
<title>Whitcombe Guard Group – Business Card</title>
<link rel="stylesheet" href="https://fonts.googleapis.com/css2?family=Source+Sans+3:wght@400;600;700&display=swap">
<style>
  :root {
    --stage-top: #2b2b2b;
    --stage-bottom: #050505;
    --card-white: #ffffff;
    --navy: #1f1d63;
    --name-blue: #2b63b6;
    --divider: #d9dce6;
    --back-center: #3c86dc;
    --back-mid: #2e54b0;
    --back-edge: #26226c;
    --mark-silver: #c8d1e2;
  }
  * { margin: 0; padding: 0; box-sizing: border-box; }
  html, body { width: 1200px; height: 900px; overflow: hidden; }
  body {
    background: linear-gradient(180deg, var(--stage-top) 0%, #161616 55%, var(--stage-bottom) 100%);
    font-family: "Source Sans 3", Arial, sans-serif;
    position: relative;
  }
  .card {
    position: absolute;
    top: 306px;
    width: 439px;
    height: 271px;
    border-radius: 10px;
    overflow: hidden;
  }
  .card-front { left: 149px; background: var(--card-white); }
  .card-back {
    left: 609px;
    background: radial-gradient(ellipse 62% 72% at 50% 42%, var(--back-center) 0%, var(--back-mid) 55%, var(--back-edge) 100%);
  }

  .brand-block {
    position: absolute;
    left: 20px; top: 88px;
    width: 168px;
    display: flex; flex-direction: column; align-items: center; gap: 10px;
  }
  .brand-dot { width: 46px; height: 46px; border-radius: 50%; background: var(--navy); }
  .brand-name {
    font-weight: 700; font-size: 14px; line-height: 1.2; letter-spacing: 0.5px;
    color: var(--navy); text-align: center; text-transform: uppercase;
  }

  .divider {
    position: absolute; left: 198px; top: 52px;
    width: 1px; height: 164px; background: var(--divider);
  }

  .details { position: absolute; left: 220px; top: 50px; color: var(--navy); white-space: nowrap; }
  .person-name { font-size: 18px; font-weight: 600; color: var(--name-blue); line-height: 20px; }
  .person-title { font-size: 12px; line-height: 14px; margin-left: 2px; }
  .address { margin-top: 12px; font-size: 13px; line-height: 18px; }
  .contact-list { list-style: none; margin-top: 11px; font-size: 13px; }
  .contact-list li { display: flex; align-items: center; height: 18px; }
  .contact-icon { width: 10px; height: 10px; margin-right: 8px; flex: none; fill: var(--navy); }

  .back-brand {
    position: absolute; left: 0; right: 0; top: 62px;
    display: flex; flex-direction: column; align-items: center; gap: 16px;
  }
  .back-dot { width: 92px; height: 92px; border-radius: 50%; background: var(--mark-silver); }
  .back-name {
    font-weight: 700; font-size: 21px; letter-spacing: 1.5px;
    color: var(--card-white); text-transform: uppercase;
  }
</style>
</head>
<body>
  <section class="card card-front">
    <div class="brand-block">
      <div class="brand-dot"></div>
      <div class="brand-name">Whitcombe<br>Guard Group</div>
    </div>
    <div class="divider"></div>
    <div class="details">
      <h1 class="person-name">Daniel R. Whitcombe</h1>
      <p class="person-title">President &amp; CEO</p>
      <p class="address">2875 E. Thistlewood Drive<br>Suite 418 Dallas, Texas 75247</p>
      <ul class="contact-list">
        <li>
          <svg class="contact-icon" viewBox="0 0 10 10" aria-hidden="true"><path d="M2 0.5 L3.6 2.8 L2.7 3.8 Q3.6 5.9 6.2 7.3 L7.2 6.4 L9.5 8 L8.3 9.5 Q4.5 9.3 1.6 6 Q0.2 4 0.6 1.6 Z"/></svg>
          602-555-0187
        </li>
        <li>
          <svg class="contact-icon" viewBox="0 0 10 10" aria-hidden="true"><path d="M0.5 2 H9.5 V8.5 H0.5 Z M1 2.4 L5 5.6 L9 2.4" stroke="#fff" stroke-width="0.8"/></svg>
          dan@whitcombeguard.com
        </li>
        <li>
          <svg class="contact-icon" viewBox="0 0 10 10" aria-hidden="true"><path d="M4 6 L6 4 M3.2 4.6 L1.6 6.2 a1.6 1.6 0 0 0 2.2 2.2 L5.4 6.8 M6.8 5.4 L8.4 3.8 a1.6 1.6 0 0 0 -2.2 -2.2 L4.6 3.2" fill="none" stroke="#1f1d63" stroke-width="1.2" stroke-linecap="round"/></svg>
          www.whitcombeguardgroup.com
        </li>
        <li>
          <svg class="contact-icon" viewBox="0 0 10 10" aria-hidden="true"><rect x="0.5" y="0.5" width="9" height="9" rx="1"/></svg>
          www.profilehub.com/in/dwhit
        </li>
      </ul>
    </div>
  </section>

  <section class="card card-back">
    <div class="back-brand">
      <div class="back-dot"></div>
      <div class="back-name">Whitcombe Guard Group</div>
    </div>
  </section>
</body>
</html>
```